Financial Advisor Graphic to Explain Proprietary and Differentiating Investment Strategy

We need a graphic that visualizes how we build a portfolio based on factors of the underlying companies. We use 8 main factors to objectively build an investment porftolio. Our colors are blues, greys (see www.tvhlgroup.com). We are thinking either a venn diagram approach or an atom approach with the factors around the middle "Core Portfolio". This is what differentiates us from everyone in the industry. This will be the key to all of our marketing

Target Market(s)

High net worth investors

Industry/Entity Type

Financial Service

Font styles to use
Serif

Requirements
Must have
• Graphic must be elegant. It is for the financial industry. It should include the following factors (in no order) to build a "Core Portfolio"
• -Counter Cyclical Industries
• -Industry Rate of Recovery
• -Price To Book
• -Absolute Risk
• -Market Capitalization
• -Liquidity
• -Dividend Yield
• -Buy Back Yield
Nice to have
• We are thinking an atom approach or a venn diagram but we are open to new ideas. It must portray the idea that we OBJECTIVELY apply these factors to stock selection to build a core portfolio for our investors. For color pallets see www.tvhlgroup.com It can go beyond the greys and blues but should not be too loud or playful. It can be high tech as long as it portrays seriousness of the financial markets
Should not have
• Can not be playful.

```html
<!DOCTYPE html>
<html lang="en">
<head>
<meta charset="utf-8">
<title>Core Portfolio Factors</title>
<link rel="stylesheet" href="https://fonts.googleapis.com/css2?family=Montserrat:wght@800;900&display=swap">
<style>
  :root {
    --bg-navy: #1e2b3a;
    --ring-fill: #141e29;
    --connector: #9aa6b2;
    --core-blue: #4aa3c8;
    --label-light: #ffffff;
    --label-dark: #111111;
    --dividend: #a9a9a9;
    --buyback: #ffffff;
    --counter: #65ae80;
    --recovery: #a3ae66;
    --price-book: #6e80aa;
    --absolute-risk: #6fa0aa;
    --market-cap: #ac8a6e;
    --liquidity: #6e89a9;
  }
  html, body {
    margin: 0;
    padding: 0;
    width: 1200px;
    height: 1077px;
    overflow: hidden;
    background: var(--bg-navy);
  }
  .factor-diagram {
    display: block;
    width: 1200px;
    height: 1077px;
  }
  .factor-label, .core-label {
    font-family: "Montserrat", Arial, sans-serif;
    font-weight: 800;
    text-anchor: middle;
    text-transform: uppercase;
  }
  .factor-label { font-size: 25px; letter-spacing: 0.5px; fill: var(--label-light); }
  .factor-label.is-dark { fill: var(--label-dark); }
  .factor-label.is-small { font-size: 21px; }
  .core-label { font-size: 56px; font-weight: 900; fill: var(--label-light); letter-spacing: 1px; }
  .connector { stroke: var(--connector); stroke-width: 5; }
  .factor-ring { fill: var(--ring-fill); stroke-width: 5; }
</style>
</head>
<body>
<svg class="factor-diagram" viewBox="0 0 1468 1317" xmlns="http://www.w3.org/2000/svg">
  <rect class="background" width="1468" height="1317" fill="var(--bg-navy)"/>

  <g class="connectors">
    <line class="connector" x1="737" y1="337" x2="737" y2="407"/>
    <line class="connector" x1="993" y1="427" x2="917" y2="495"/>
    <line class="connector" x1="975" y1="657" x2="1045" y2="657"/>
    <line class="connector" x1="902" y1="800" x2="982" y2="868"/>
    <line class="connector" x1="737" y1="872" x2="737" y2="942"/>
    <line class="connector" x1="570" y1="806" x2="492" y2="878"/>
    <line class="connector" x1="422" y1="657" x2="493" y2="657"/>
    <line class="connector" x1="472" y1="425" x2="553" y2="492"/>
  </g>

  <g class="core">
    <circle cx="735" cy="633" r="215" fill="var(--core-blue)"/>
    <text class="core-label" x="730" y="622">Core</text>
    <text class="core-label" x="735" y="668">Portfolio</text>
  </g>

  <g class="factor factor--dividend">
    <circle class="factor-ring" cx="735" cy="182" r="138" stroke="var(--dividend)"/>
    <circle cx="735" cy="182" r="108" fill="var(--dividend)"/>
    <text class="factor-label is-dark" x="735" y="180">Dividend</text>
    <text class="factor-label is-dark" x="738" y="202">Yield</text>
  </g>

  <g class="factor factor--buyback">
    <circle class="factor-ring" cx="1110" cy="323" r="138" stroke="var(--buyback)"/>
    <circle cx="1110" cy="323" r="108" fill="var(--buyback)"/>
    <text class="factor-label is-dark" x="1109" y="328">Buy Back</text>
    <text class="factor-label is-dark" x="1112" y="350">Yield</text>
  </g>

  <g class="factor factor--counter">
    <circle class="factor-ring" cx="1205" cy="652" r="138" stroke="var(--counter)"/>
    <circle cx="1205" cy="652" r="108" fill="var(--counter)"/>
    <text class="factor-label" x="1205" y="638">Counter</text>
    <text class="factor-label" x="1205" y="664">Cyclical</text>
    <text class="factor-label" x="1208" y="690">Industries</text>
  </g>

  <g class="factor factor--recovery">
    <circle class="factor-ring" cx="1100" cy="975" r="138" stroke="var(--recovery)"/>
    <circle cx="1100" cy="975" r="108" fill="var(--recovery)"/>
    <text class="factor-label" x="1098" y="970">Industry</text>
    <text class="factor-label" x="1099" y="996">Rate of</text>
    <text class="factor-label" x="1102" y="1022">Recovery</text>
  </g>

  <g class="factor factor--price-book">
    <circle class="factor-ring" cx="730" cy="1105" r="138" stroke="var(--price-book)"/>
    <circle cx="730" cy="1105" r="108" fill="var(--price-book)"/>
    <text class="factor-label" x="729" y="1103">Price</text>
    <text class="factor-label" x="732" y="1125">To Book</text>
  </g>

  <g class="factor factor--absolute-risk">
    <circle class="factor-ring" cx="370" cy="975" r="138" stroke="var(--absolute-risk)"/>
    <circle cx="370" cy="975" r="108" fill="var(--absolute-risk)"/>
    <text class="factor-label" x="371" y="979">Absolute</text>
    <text class="factor-label" x="374" y="1001">Risk</text>
  </g>

  <g class="factor factor--market-cap">
    <circle class="factor-ring" cx="263" cy="652" r="138" stroke="var(--market-cap)"/>
    <circle cx="263" cy="652" r="108" fill="var(--market-cap)"/>
    <text class="factor-label is-small" x="259" y="657">Market</text>
    <text class="factor-label is-small" x="262" y="676">Capitalization</text>
  </g>

  <g class="factor factor--liquidity">
    <circle class="factor-ring" cx="366" cy="317" r="138" stroke="var(--liquidity)"/>
    <circle cx="366" cy="317" r="108" fill="var(--liquidity)"/>
    <text class="factor-label" x="366" y="330">Liquidity</text>
  </g>
</svg>
</body>
</html>
```